Hong Kong residential leasing and sales company needs a website design

Hong Kong has many competitive real estate agents. The majority of us have the same listings so, besides the team and experience, a website is what makes us stand out. A first impression. We need our website to be user friendly, informative and to have a wow factor. Most sites are generic so whilst we are close to accepting that maybe that's the only formula which works....we would like to see if we're missing something! Our clients are a mix of International users of all ages but probably ultimately 35+.. We have a logo (attached) which we would like to keep - designed by artmarketly. Flexible with colours except red.
examples of our competitors are:
http://www.brindlewoodestates.example
http://www.nuvo.example/home
http://www.premierdwellingsvx.example
http://www.orchid-lettings.example
http://www.tidemark-harrowgates.example
We were thinking of having the following in a menu bar with drop downs for most...some more than others. Home / For Sale / For Rent / Property 101 / About us / Contact Us ..
Look forward to seeing your ideas. Thanks in advance.

```html
<!DOCTYPE html>
<html lang="en">
<head>
<meta charset="utf-8">
<title>Lanterne Residences</title>
<link href="https://fonts.googleapis.com/css2?family=Marcellus&family=Roboto:wght@400;500;700&display=swap" rel="stylesheet">
<style>
:root{
  --purple:#6a3d8f;
  --ink:#333333;
  --muted:#555555;
  --panel:rgba(236,236,238,.9);
  --dark:#0d0d0d;
  --white:#ffffff;
  --grey-line:#d8d8d8;
}
*{margin:0;padding:0;box-sizing:border-box}
html,body{width:951px;height:1200px;overflow:hidden;background:var(--white)}
body{position:relative;font-family:Arial,Helvetica,sans-serif;color:var(--ink)}
.site-header{position:absolute;left:0;top:0;width:951px;height:140px;background:var(--white)}
.nav-item{position:absolute;top:80px;font-family:'Marcellus',serif;font-size:17px;color:var(--ink);letter-spacing:.3px}
.nav-home{position:absolute;left:27px;top:0;width:83px;height:120px;background:var(--purple);border-bottom:6px solid #444}
.nav-home span{position:absolute;left:0;right:0;top:80px;text-align:center;color:var(--white);font-family:'Marcellus',serif;font-size:17px}
.brand{position:absolute;left:395px;top:58px;width:160px;text-align:center;font-family:'Marcellus',serif;font-size:22px;letter-spacing:3px;color:var(--ink);line-height:1.05}
.brand-mark{display:block;width:14px;height:14px;background:var(--purple);margin:0 auto 6px}
.hero{position:absolute;left:0;top:140px;width:951px;height:903px;background:linear-gradient(180deg,#1a2230 0%,#2b3340 35%,#5a5a55 70%,#8a7a5a 90%,#3a3a38 100%)}
.search-panel{position:absolute;left:29px;top:184px;width:893px;height:117px;background:var(--panel)}
.keyword{position:absolute;left:43px;top:21px;width:667px;height:35px;background:var(--white);font-family:'Marcellus',serif;font-size:18px;padding:8px 18px;color:var(--ink)}
.select{position:absolute;top:68px;width:155px;height:30px;background:var(--white);font-family:'Roboto',sans-serif;font-size:14px;color:var(--purple);padding:6px 16px}
.select::after{content:"";position:absolute;right:15px;top:11px;border-left:5px solid transparent;border-right:5px solid transparent;border-top:8px solid var(--purple)}
.search-btn{position:absolute;left:722px;top:21px;width:133px;height:77px;background:var(--purple);color:var(--white);font-family:'Roboto',sans-serif;font-weight:700;font-size:13px;text-align:center}
.search-btn svg{display:block;margin:6px auto 4px}
.featured-title{position:absolute;left:29px;top:349px;width:893px;height:47px;background:var(--dark);color:var(--white);font-family:'Marcellus',serif;font-size:31px;font-weight:400;padding:5px 26px}
.featured-panel{position:absolute;left:29px;top:396px;width:893px;height:592px;background:var(--panel)}
.card{position:absolute;width:188px;height:247px;background:var(--white);border:1px solid var(--grey-line);overflow:hidden}
.card-photo{position:absolute;left:7px;top:7px;width:174px;height:131px}
.ribbon{position:absolute;left:-34px;top:22px;width:130px;height:24px;background:#3a3a3a;color:var(--white);font-size:11.5px;text-align:center;line-height:24px;transform:rotate(-45deg)}
.card-title{position:absolute;left:7px;top:148px;font-family:'Roboto',sans-serif;font-weight:500;font-size:13.5px;color:var(--purple);white-space:nowrap}
.card-specs{position:absolute;left:9px;top:170px;font-size:11.5px;line-height:14px;color:var(--muted)}
.site-footer{position:absolute;left:0;top:1043px;width:951px;height:157px;background:var(--white)}
.foot-brand{position:absolute;left:40px;top:42px;width:100px;text-align:center;font-family:'Marcellus',serif;font-size:18px;letter-spacing:2px;line-height:1.05;color:var(--ink)}
.foot-brand .brand-mark{width:12px;height:12px}
.foot-blurb{position:absolute;left:147px;top:37px;font-size:11.5px;line-height:14px;color:#8a8a8a}
.copyright{position:absolute;left:41px;top:117px;font-size:10.5px;color:var(--ink)}
.foot-links{position:absolute;top:33px;font-size:11.5px;line-height:18px;color:var(--ink);list-style:none}
.social{position:absolute;top:28px;width:23px;height:23px;border-radius:50%;background:#111}
.contact-info{position:absolute;left:672px;top:63px;font-size:10.5px;line-height:13.5px;color:var(--ink);white-space:nowrap}
</style>
</head>
<body>
<header class="site-header">
  <div class="nav-home"><span>HOME</span></div>
  <div class="nav-item" style="left:134px">PROPERTY 101</div>
  <div class="nav-item" style="left:289px">FOR SALE</div>
  <div class="brand"><span class="brand-mark"></span>LANTERNE<br><span style="font-size:10px;letter-spacing:4px">RESIDENCES</span></div>
  <div class="nav-item" style="left:586px">FOR RENT</div>
  <div class="nav-item" style="left:705px">ABOUT US</div>
  <div class="nav-item" style="left:827px">CONTACT</div>
</header>

<div class="hero" role="img" aria-label="Night view of Hong Kong residential towers with lit windows"></div>

<section class="search-panel">
  <div class="keyword">Keyword Search</div>
  <div class="select" style="left:43px">Property Type</div>
  <div class="select" style="left:214px">Sale/Rent</div>
  <div class="select" style="left:384px">Location</div>
  <div class="select" style="left:555px">Price Range</div>
  <div class="search-btn">
    <svg width="44" height="44" viewBox="0 0 44 44"><circle cx="19" cy="19" r="14" fill="none" stroke="#fff" stroke-width="4"/><line x1="29" y1="29" x2="40" y2="40" stroke="#fff" stroke-width="5" stroke-linecap="round"/></svg>
    SEARCH
  </div>
</section>

<h2 class="featured-title">FEATURED PROPERTIES</h2>
<section class="featured-panel"></section>

<article class="card" style="left:60px;top:428px">
  <div class="card-photo" role="img" aria-label="Bright living room with city-view windows" style="background:linear-gradient(180deg,#d8d6d0,#8a7d6c)"></div>
  <div class="ribbon">For Sale</div>
  <div class="card-title">The Crestline - Block 02</div>
  <div class="card-specs">Gross Area: 3,850 sq.ft.<br>Saleable Area: 2,969 sq.ft.<br>Bedrooms: 4 (2 Ensuites)<br>Bathrooms: 3.5<br>Price: HK$ 260,000,000</div>
</article>
<article class="card" style="left:274px;top:428px">
  <div class="card-photo" role="img" aria-label="Living room with red sofa and harbour view" style="background:linear-gradient(180deg,#c9ccd0,#6e5a56)"></div>
  <div class="ribbon">For Rent</div>
  <div class="card-title">Villa Serena - Apartment B</div>
  <div class="card-specs">Gross Area: 2,700 sq.ft.<br>Saleable Area: 2,512 sq.ft.<br>Bedrooms: 3 (1 Ensuite)<br>Bathrooms: 2<br>Price: HK$ 75,000,000</div>
</article>
<article class="card" style="left:489px;top:428px">
  <div class="card-photo" role="img" aria-label="City skyline above a green racecourse" style="background:linear-gradient(180deg,#7fa6d8 0%,#b8c6d4 40%,#5d7a56 80%,#3e5a3a)"></div>
  <div class="ribbon">For Sale</div>
  <div class="card-title">Paddock Tower</div>
  <div class="card-specs">Gross Area: 3,850 sq.ft.<br>Saleable Area: 2,969 sq.ft.<br>Bedrooms: 4 (2 Ensuites)<br>Bathrooms: 3.5<br>Price: HK$ 260,000,000</div>
</article>
<article class="card" style="left:702px;top:428px">
  <div class="card-photo" role="img" aria-label="Living room with ceiling fan and cream sofas" style="background:linear-gradient(180deg,#d6d1c8,#6a5648)"></div>
  <div class="ribbon">For Sale</div>
  <div class="card-title">Kingsley Mansion</div>
  <div class="card-specs">Gross Area: 4,200 sq.ft.<br>Saleable Area: 3,273 sq.ft.<br>Bedrooms: 5 (3 Ensuites)<br>Bathrooms: 4<br>Price: HK$ 77,000,000</div>
</article>

<article class="card" style="left:60px;top:709px">
  <div class="card-photo" role="img" aria-label="High-rise towers under a blue sky" style="background:linear-gradient(180deg,#5d8fc8,#b9c9d8 60%,#6a7068)"></div>
  <div class="ribbon">For Rent</div>
  <div class="card-title">Harbour Terrace 3</div>
  <div class="card-specs">Gross Area: 3,850 sq.ft.<br>Saleable Area: 2,969 sq.ft.<br>Bedrooms: 4 (2 Ensuites)<br>Bathrooms: 3.5<br>Price: HK$ 260,000,000</div>
</article>
<article class="card" style="left:274px;top:709px">
  <div class="card-photo" role="img" aria-label="Warm living room with grey sofas" style="background:linear-gradient(180deg,#c8b8a2,#6b5a4a)"></div>
  <div class="ribbon">For Sale</div>
  <div class="card-title">Graceful Court</div>
  <div class="card-specs">Gross Area: 2,700 sq.ft.<br>Saleable Area: 2,512 sq.ft.<br>Bedrooms: 3 (1 Ensuite)<br>Bathrooms: 2<br>Price: HK$ 75,000,000</div>
</article>
<article class="card" style="left:489px;top:709px">
  <div class="card-photo" role="img" aria-label="White modern kitchen" style="background:linear-gradient(180deg,#e6e6e2,#a8a7a0)"></div>
  <div class="ribbon">For Sale</div>
  <div class="card-title">Westmoor Towers - Block C</div>
  <div class="card-specs">Gross Area: 3,850 sq.ft.<br>Saleable Area: 2,969 sq.ft.<br>Bedrooms: 4 (2 Ensuites)<br>Bathrooms: 3.5<br>Price: HK$ 260,000,000</div>
</article>
<article class="card" style="left:702px;top:709px">
  <div class="card-photo" role="img" aria-label="Living room with ceiling fan and cream sofas" style="background:linear-gradient(180deg,#d6d1c8,#6a5648)"></div>
  <div class="ribbon">For Rent</div>
  <div class="card-title">Kingsley Mansion</div>
  <div class="card-specs">Gross Area: 4,200 sq.ft.<br>Saleable Area: 3,273 sq.ft.<br>Bedrooms: 5 (3 Ensuites)<br>Bathrooms: 4<br>Price: HK$ 77,000,000</div>
</article>

<footer class="site-footer">
  <div class="foot-brand"><span class="brand-mark"></span>LANTERNE<br><span style="font-size:8px;letter-spacing:3px">RESIDENCES</span></div>
  <p class="foot-blurb">Ut wisi enim ad minim veniam,<br>quis nostrud exerci tation<br>ullamcorper suscipit lobortis nisl<br>ut aliquip ex ea commodo consequat.</p>
  <p class="copyright">Copyright ©2014 Lanterne Residences. All rights reserved.</p>
  <ul class="foot-links" style="left:406px"><li>Home</li><li>About Us</li><li>For Sale</li><li>For Rent</li><li>Property 101</li></ul>
  <ul class="foot-links" style="left:498px"><li>Contact</li><li>Privacy Policy</li><li>Terms</li><li>Disclaimer</li></ul>
  <span class="social" style="left:670px"></span>
  <span class="social" style="left:701px"></span>
  <span class="social" style="left:732px"></span>
  <span class="social" style="left:763px"></span>
  <span class="social" style="left:794px"></span>
  <p class="contact-info">2204-2205 Meridian Commerce Centre, 18<br>Lantern Lane, Central, Hong Kong<br>Tel: +852 2000 4817 / Fax: +852 3000 5262<br>info@premierdwellingsvx.example</p>
</footer>
</body>
</html>
```